Cartwise.io

Australian based application building technology company. website (cartwise.io) servicing the retail and shopping industries, IoT
Similar services to https://fenvo.com/.

Target Market(s)

Technology Retail

Industry/Entity Type

It Company

Number of Pages Required

2 page

Font styles to use
Other font styles liked:
• We will supply

Colors
ec1f27

Requirements
Must have
• responsive, extra small, small, medium, large, wide
Nice to have
• Modern, sophisticated, current and ON trende
Should not have
• Over saturation, keep it simple, smart and easy navigation

```html
<!DOCTYPE html>
<html lang="en">
<head>
<meta charset="utf-8">
<title>Cartwise – Retail Navigation and Analytics</title>
<link rel="stylesheet" href="https://fonts.googleapis.com/css2?family=Raleway:wght@300;400;500;600&family=Open+Sans:ital,wght@0,400;0,600;0,700;1,400&display=swap">
<style>
:root{
  --red:#ec1f27;
  --red-deep:#b5121a;
  --red-band:#e0262e;
  --ink:#222222;
  --text:#666666;
  --muted:#999999;
  --line:#e3e3e3;
  --grey-bg:#f2f2f2;
  --dark:#2b2b2b;
  --white:#ffffff;
}
*{box-sizing:border-box;margin:0;padding:0}
html,body{width:1200px;height:3550px;overflow:hidden}
body{font-family:"Open Sans",Arial,sans-serif;color:var(--text);background:var(--white);position:relative}
.section{position:absolute;left:0;width:1200px;overflow:hidden}
.abs{position:absolute}
h2{font-family:"Raleway",Helvetica,sans-serif;font-weight:400;font-size:29px;color:var(--ink)}
p{font-size:13px;line-height:26px}
.btn{display:inline-flex;align-items:center;justify-content:center;border-radius:24px;font-family:"Open Sans",Arial,sans-serif;font-weight:700;font-size:12px;letter-spacing:.5px;text-transform:uppercase}

/* header + hero */
.hero{top:0;height:545px;background:#a4121a}
.hero-visual{inset:0;background:radial-gradient(ellipse at 50% 45%,#d52028 0%,#a4121a 70%,#7d0c12 100%)}
.brand{display:flex;align-items:center;gap:10px;font-family:"Raleway",Helvetica,sans-serif;font-weight:600;font-size:27px;letter-spacing:.5px}
.brand-dot{width:30px;height:30px;border-radius:50%;border:3px solid currentColor}
.site-header{position:absolute;inset:0 0 auto 0;height:100px;z-index:2}
.site-header .brand{position:absolute;left:97px;top:30px;color:var(--white)}
.main-nav{position:absolute;left:392px;top:38px;display:flex;align-items:center;gap:27px;font-size:14px;font-weight:600;color:var(--white);text-transform:uppercase}
.main-nav .active{color:#ff8a8a}
.sign-in{display:flex;align-items:center;gap:6px;border:2px solid var(--white);border-radius:20px;padding:5px 14px;font-size:13px}
.hero-title{left:0;width:1200px;top:446px;text-align:center;font-family:"Raleway",Helvetica,sans-serif;font-weight:300;font-size:34px;color:var(--white)}

/* navigation intro */
.intro{top:545px;height:485px}
.device-pair{left:47px;top:75px;width:521px;height:303px;background:linear-gradient(160deg,#3a8fd8 0%,#7db3e0 50%,#e6e6e6 100%);border-radius:10px}
.intro h2{position:absolute;left:632px;top:93px}
.intro p{position:absolute;left:632px;top:148px;width:530px}
.intro .btn{position:absolute;left:632px;top:284px;width:197px;height:46px;border:2px solid var(--red);color:var(--red)}

/* pillars band */
.pillars{top:1030px;height:395px}
.pillars-bg{inset:0;background:linear-gradient(110deg,#4b4540 0%,#6b6157 45%,#3c3733 100%)}
.pillar{position:absolute;top:58px;width:320px;text-align:center;color:var(--white)}
.pillar .ring{width:180px;height:180px;margin:0 auto;border:2px solid var(--white);border-radius:50%;display:flex;align-items:center;justify-content:center;background:rgba(255,255,255,.04)}
.pillar h3{margin-top:40px;font-family:"Raleway",Helvetica,sans-serif;font-weight:400;font-size:22px;line-height:33px}

/* features */
.features{top:1425px;height:532px}
.features h2{position:absolute;left:97px;top:68px}
.features .lead{position:absolute;left:97px;top:125px;width:460px}
.feature-list{position:absolute;left:97px;top:200px;list-style:none}
.feature-list li{display:flex;align-items:center;gap:17px;height:76px;margin-bottom:10px;font-size:16px;color:#333}
.feature-list .icon{width:76px;height:76px;border:1px solid var(--line);border-radius:50%;display:flex;align-items:center;justify-content:center}
.floor-plan{left:580px;top:83px;width:592px;height:338px;border-radius:12px;background:linear-gradient(#111 0 6%,#e8ecef 6% 88%,#c9c9c9 88%)}

/* testimonials */
.testimonials{top:1957px;height:339px;background:linear-gradient(135deg,var(--red-band),#d41d25 60%,var(--red-band))}
.testimonials h2{position:absolute;width:1200px;top:42px;text-align:center;color:var(--white)}
.slider-arrow{position:absolute;top:150px;width:38px;height:38px;border:1px solid rgba(255,255,255,.7);border-radius:50%;display:flex;align-items:center;justify-content:center}
.quote{position:absolute;top:126px;width:330px;color:var(--white)}
.quote .avatar{position:absolute;left:0;top:0;width:76px;height:76px;border-radius:50%;border:3px solid var(--white);background:linear-gradient(#e7ccb7,#b58d72)}
.quote blockquote{margin-left:96px;font-size:12px;font-style:italic;line-height:22px;position:relative}
.quote blockquote::before{content:"\201C";position:absolute;left:-16px;top:-8px;font-size:30px;font-style:normal;font-family:Georgia,serif}
.quote .name{margin:10px 0 0 96px;font-size:10px;font-weight:700;text-transform:uppercase}
.quote .role{margin-left:96px;font-size:10px;font-style:italic}

/* capabilities */
.capabilities{top:2296px;height:552px;background:var(--grey-bg)}
.capabilities h2{position:absolute;width:1200px;top:74px;text-align:center}
.capabilities p{position:absolute;left:290px;width:620px;top:126px;text-align:center}
.hands{left:284px;top:208px;width:639px;height:344px;background:linear-gradient(90deg,#d9b59e,#eed4c2 30%,#eed4c2 70%,#d3ad94)}
.tablet{left:370px;top:225px;width:460px;height:300px;background:#111;border-radius:22px;padding:18px 24px}
.tablet svg{display:block;width:100%;height:100%;background:var(--white)}

/* call to action */
.cta{top:2848px;height:295px}
.cta-bg{inset:0;background:linear-gradient(100deg,#2a2a2a 0%,#3d3d3d 55%,#4e5258 100%)}
.cta h2{position:absolute;width:1200px;top:48px;text-align:center;color:var(--white)}
.cta p{position:absolute;left:290px;width:620px;top:102px;text-align:center;color:#e5e5e5}
.cta .btn{position:absolute;left:510px;top:190px;width:180px;height:46px;background:var(--red);color:var(--white)}

/* footer */
.site-footer{top:3143px;height:407px;background:var(--white)}
.site-footer .brand{position:absolute;left:90px;top:92px;color:var(--red);font-size:26px}
.contact-list{position:absolute;left:97px;top:162px;list-style:none;font-size:11px;line-height:17px;color:#555}
.contact-list li{display:flex;gap:16px;margin-bottom:16px}
.contact-list svg{flex:none;margin-top:2px}
.divider{position:absolute;top:90px;width:1px;height:230px;background:var(--line)}
.footer-col{position:absolute;top:88px}
.footer-col h4{font-family:"Raleway",Helvetica,sans-serif;font-weight:600;font-size:17px;color:var(--ink);margin-bottom:22px}
.footer-col ul{list-style:none;font-size:12px;line-height:29px;color:#555}
.footer-col p{font-size:12px;line-height:22px;width:270px;color:#555}
.email-field{margin-top:18px;width:260px;height:36px;border:1px solid #ddd;font-size:11px;padding:10px;color:#888}
.footer-col .btn{margin-top:20px;width:108px;height:34px;background:var(--red);color:var(--white);font-size:11px}
.copyright{position:absolute;left:0;top:337px;width:1200px;height:70px;border-top:1px solid var(--line);text-align:center;font-size:12px;line-height:70px;color:#666}
</style>
</head>
<body>

<section class="section hero">
  <div class="abs hero-visual" role="img" aria-label="Two blue retail beacons either side of a smartphone playing an indoor store map video"></div>
  <header class="site-header">
    <div class="brand"><span class="brand-dot"></span>CARTWISE</div>
    <nav class="main-nav">
      <span class="active">Home</span><span>About</span><span>Products</span><span>Resources</span><span>Support</span><span>Contact</span>
      <svg width="16" height="16" viewBox="0 0 16 16" fill="none" stroke="#fff" stroke-width="2"><circle cx="6.5" cy="6.5" r="5"/><path d="M10.5 10.5l4 4"/></svg>
      <span class="sign-in"><svg width="10" height="12" viewBox="0 0 10 12" fill="#fff"><rect x="0" y="5" width="10" height="7" rx="1"/><path d="M2 5V3.5a3 3 0 016 0V5" fill="none" stroke="#fff" stroke-width="1.6"/></svg>Sign in</span>
    </nav>
  </header>
  <div class="abs hero-title">This will make you Cartwise</div>
</section>

<section class="section intro">
  <div class="abs device-pair" role="img" aria-label="Laptop with beacon signal map and smartphone showing the store app"></div>
  <h2>Navigation and Indoor Analytics</h2>
  <p>Nemo enim ipsam voluptatem quia voluptas sit aspernatur aut odit aut fugit, sed quia consequuntur magni dolores eos qui ratione voluptatem sequi nesciunt. Neque porro quisquam est, qui dolorem ipsum quia dolor sit amet consectetur, adipisci velit, sed quia non num.</p>
  <a class="btn">Upgrade your app</a>
</section>

<section class="section pillars">
  <div class="abs pillars-bg" role="img" aria-label="Darkened photo of hands using a tablet on a wooden desk"></div>
  <div class="pillar" style="left:105px">
    <div class="ring"><svg width="46" height="64" viewBox="0 0 46 64"><path d="M23 2C11 2 2 11 2 23c0 16 21 39 21 39s21-23 21-39C44 11 35 2 23 2z" fill="#fff"/><circle cx="23" cy="23" r="8" fill="#5a534c"/></svg></div>
    <h3>Map to Exact<br>Location</h3>
  </div>
  <div class="pillar" style="left:410px">
    <div class="ring"><svg width="62" height="62" viewBox="0 0 62 62"><circle cx="31" cy="31" r="27" fill="none" stroke="#fff" stroke-width="6"/><path d="M31 15v17h12" fill="none" stroke="#fff" stroke-width="6" stroke-linecap="round"/></svg></div>
    <h3>Promote specific to<br>time and Space</h3>
  </div>
  <div class="pillar" style="left:749px">
    <div class="ring"><svg width="78" height="62" viewBox="0 0 78 62" fill="none" stroke="#fff" stroke-width="5"><path d="M8 24c0-10 10-18 24-18s24 8 24 18-10 18-24 18c-3 0-6 0-8-1L10 48l4-11c-4-3-6-8-6-13z"/><path d="M58 22c8 3 14 9 14 16 0 5-2 9-6 12l3 9-11-6c-3 1-5 1-8 1-9 0-17-4-20-9"/></svg></div>
    <h3>Interact LIVE at<br>Product level</h3>
  </div>
</section>

<section class="section features">
  <h2>Cartwise Features</h2>
  <p class="lead">Nemo enim ipsam voluptatem quia voluptas sit aspernatur aut odit aut fugit, sed quia consequuntur magni dolores eos qui ratione.</p>
  <ul class="feature-list">
    <li><span class="icon"><svg width="34" height="30" viewBox="0 0 34 30" fill="none" stroke="#ec1f27" stroke-width="3"><circle cx="12" cy="17" r="6"/><circle cx="26" cy="8" r="4"/><path d="M12 5v4M12 25v4M0 17h4M20 17h4M26 0v3M26 13v3M19 8h3M30 8h3"/></svg></span>Establish first contact in seconds</li>
    <li><span class="icon"><svg width="34" height="28" viewBox="0 0 34 28" fill="none" stroke="#ec1f27" stroke-width="3"><path d="M3 11c0-5 5-9 12-9s12 4 12 9-5 9-12 9l-8 4 2-6c-4-2-6-4-6-7z"/><path d="M28 10c3 2 4 4 4 6 0 3-2 5-4 6l1 4-5-2"/></svg></span>Interact Immediately and Promote</li>
    <li><span class="icon"><svg width="30" height="26" viewBox="0 0 30 26" fill="#ec1f27"><rect x="4" y="12" width="4" height="12"/><rect x="11" y="6" width="4" height="18"/><rect x="18" y="9" width="4" height="15"/><rect x="25" y="3" width="4" height="21"/><rect x="0" y="24" width="30" height="2"/></svg></span>Analytics for real-time sales</li>
  </ul>
  <div class="abs floor-plan" role="img" aria-label="Laptop displaying an indoor floor plan with a blue location marker and route"></div>
</section>

<section class="section testimonials">
  <h2>Client Testimonials</h2>
  <span class="slider-arrow" style="left:26px"><svg width="10" height="14" viewBox="0 0 10 14" fill="none" stroke="#fff" stroke-width="2"><path d="M8 1L2 7l6 6"/></svg></span>
  <span class="slider-arrow" style="left:1134px"><svg width="10" height="14" viewBox="0 0 10 14" fill="none" stroke="#fff" stroke-width="2"><path d="M2 1l6 6-6 6"/></svg></span>
  <div class="quote" style="left:97px">
    <div class="avatar" role="img" aria-label="Client portrait photo"></div>
    <blockquote>At vero eos et accusamus et iusto odio dignissimos ducimus qui blanditiis praesent ium voluptatum deleniti atque corrupt dolores et quas molestias.</blockquote>
    <div class="name">Lena Marwick</div><div class="role">Financial Services Professional</div>
  </div>
  <div class="quote" style="left:442px">
    <div class="avatar" role="img" aria-label="Client portrait photo"></div>
    <blockquote>At vero eos et accusamus et iusto odio dignissimos ducimus qui blanditiis praesent ium voluptatum deleniti atque corrupt dolores et quas molestias.</blockquote>
    <div class="name">Tomas R. Halvorsen</div><div class="role">National Urban Fellow at the Harbour</div>
  </div>
  <div class="quote" style="left:790px">
    <div class="avatar" role="img" aria-label="Client portrait photo"></div>
    <blockquote>At vero eos et accusamus et iusto odio dignissimos ducimus qui blanditiis praesent ium voluptatum deleniti atque corrupt dolores et quas molestias.</blockquote>
    <div class="name">Priya Castell</div><div class="role">Creative Strategist | Entrepreneur &amp; Upcoming</div>
  </div>
</section>

<section class="section capabilities">
  <h2>Online Capabilities and Analytics</h2>
  <p>At vero eos et accusamus et iusto odio dignissimos ducimus qui blanditiis praesentium voluptatum deleniti atque corrupti quos dolores et quas molestias excepturi sint occaecati cupid</p>
  <div class="abs hands" role="img" aria-label="Two hands holding a tablet"></div>
  <div class="abs tablet">
    <svg viewBox="0 0 412 264" role="img" aria-label="Bar chart: number of officers in Brookdale, 1993 to 2001">
      <text x="40" y="16" font-family="Open Sans, Arial, sans-serif" font-size="11" font-weight="700" fill="#111">Figure 1. Number of officers in Brookdale, 1993 to 2001</text>
      <g stroke="#ddd" stroke-width="1">
        <line x1="44" y1="40" x2="400" y2="40"/><line x1="44" y1="80" x2="400" y2="80"/><line x1="44" y1="120" x2="400" y2="120"/><line x1="44" y1="160" x2="400" y2="160"/><line x1="44" y1="200" x2="400" y2="200"/>
      </g>
      <line x1="44" y1="30" x2="44" y2="240" stroke="#333"/><line x1="44" y1="240" x2="400" y2="240" stroke="#333"/>
      <g fill="#d4161e">
        <rect x="56" y="75" width="22" height="165"/><rect x="95" y="82" width="22" height="158"/><rect x="134" y="95" width="22" height="145"/><rect x="173" y="110" width="22" height="130"/><rect x="212" y="104" width="22" height="136"/><rect x="251" y="90" width="22" height="150"/><rect x="290" y="84" width="22" height="156"/><rect x="329" y="72" width="22" height="168"/><rect x="368" y="68" width="22" height="172"/>
      </g>
      <g font-family="Open Sans, Arial, sans-serif" font-size="8" fill="#333">
        <text x="58" y="254">1993</text><text x="97" y="254">1994</text><text x="136" y="254">1995</text><text x="175" y="254">1996</text><text x="214" y="254">1997</text><text x="253" y="254">1998</text><text x="292" y="254">1999</text><text x="331" y="254">2000</text><text x="370" y="254">2001</text>
        <text x="30" y="43">60</text><text x="30" y="83">50</text><text x="30" y="123">40</text><text x="30" y="163">30</text><text x="30" y="203">20</text>
      </g>
    </svg>
  </div>
</section>

<section class="section cta">
  <div class="abs cta-bg" role="img" aria-label="Darkened photo of a desk with analytics charts on screen"></div>
  <h2>Ready to get started?</h2>
  <p>At vero eos et accusamus et iusto odio dignissimos ducimus qui blanditiis praesentium voluptatum deleniti atque corrupti quos dolores et quas molestias excepturi sint occaecati cupid</p>
  <a class="btn">Get started</a>
</section>

<footer class="section site-footer">
  <div class="brand"><span class="brand-dot"></span>CARTWISE</div>
  <ul class="contact-list">
    <li><svg width="12" height="15" viewBox="0 0 12 15" fill="#ec1f27"><path d="M6 0C2.7 0 0 2.6 0 5.8 0 10 6 15 6 15s6-5 6-9.2C12 2.6 9.3 0 6 0zm0 8a2.2 2.2 0 110-4.4A2.2 2.2 0 016 8z"/></svg><span>4820 Harbour Lane<br>Brookvale, NSW 2100</span></li>
    <li><svg width="13" height="13" viewBox="0 0 13 13" fill="#ec1f27"><path d="M2.6 0l2.2 3-1.3 1.6a8 8 0 004.9 4.9L10 8.2l3 2.2-1.5 2.5C5.5 13 0 7.5.1 1.5z"/></svg><span>1 800 555 0147</span></li>
    <li><svg width="13" height="13" viewBox="0 0 13 13" fill="#ec1f27"><rect x="0" y="2" width="13" height="10" rx="1"/><rect x="3" y="0" width="7" height="4" fill="#fff" stroke="#ec1f27"/></svg><span>1 800 555 0192</span></li>
    <li><svg width="13" height="10" viewBox="0 0 13 10" fill="#ec1f27"><rect width="13" height="10" rx="1"/><path d="M0 1l6.5 5L13 1" fill="none" stroke="#fff" stroke-width="1.2"/></svg><span>info@cartwise.io</span></li>
  </ul>
  <span class="divider" style="left:360px"></span>
  <span class="divider" style="left:561px"></span>
  <span class="divider" style="left:793px"></span>
  <div class="footer-col" style="left:400px">
    <h4>Information</h4>
    <ul><li>About us</li><li>Tile Calculator</li><li>Your wishlist</li><li>Blog</li><li>Advice Centre</li><li>Terms of Use</li></ul>
  </div>
  <div class="footer-col" style="left:596px">
    <h4>Resources</h4>
    <ul><li>Quick Start Guide</li><li>Dev Resources</li><li>Physical Web Info</li><li>Best Practices</li><li>Scanners/Browsers</li><li>Knowledge Base</li></ul>
  </div>
  <div class="footer-col" style="left:840px">
    <h4>Newsletter Subscription</h4>
    <p>Register your email address to get information about us</p>
    <div class="email-field">Email Address</div>
    <a class="btn">Subscribe</a>
  </div>
  <div class="copyright">Copyrights © 2017, Cartwise . All Rights Reserved &nbsp;|&nbsp; Privacy Policy | Terms of Use | Feedback</div>
</footer>

</body>
</html>
```